Automotive Parts Company Business Card/Logo Design

We need a logo/business card for a new automotive parts and accessories company which is based in Barbados. The company will only have an online presence and this will reduce our overheads and allow us to pass potential savings to our customers.

We will offer most automotive parts which include, but are not limited to, accessories, exterior, interior, body parts.

We want to appeal to a very wide audience and we're looking for a modern, clean and bold design to make the company seem very professional. Our logo and facebook page will be our only customer facing items. So it is essential that these are done correctly.

The design should really communicate that we can provide premium car parts at affordable prices for all types of cars e.g. European and Japanese.

We will stock items and also source hard to get and unique pieces. We aim to not just be another shop that sells parts. But we want to work with our customers to achieve their car goals.

The company name is GearVista and our slogan is Quality Parts At Affordable Prices.
The design should be very modern, clean and bold.

I've included examples of some of the business cards I like as well as images of car products.
Updates

Dear Designers,

I've uploaded some samples of some business card/logo designs I like. Please have a look at the project brief. Just to reiterate, I am looking for a clean, modern design.

Thanks,

Rohan

Dear Designers,

Please note the Apr 14th deadline is soon approaching.

Also note the business card is double-sided.

I look forward to working with you.

Thanks,

Rohan

Target Market(s)

20 - 30 (young professionals, younger generation with disposible income) and then then all other markets

Industry/Entity Type

Automotive

Contact Information for Business Card

Rohan Melwanikar
GearVista
Quality Parts At Affordable Prices
https://www.examplesocial.test/gearvistabq
246-319-8042
gearvistabq@mailbox-example.test

```html
<!DOCTYPE html>
<html lang="en">
<head>
<meta charset="utf-8">
<title>GearVista Business Card</title>
<link rel="stylesheet" href="https://fonts.googleapis.com/css2?family=Open+Sans:wght@400;600;700&display=swap">
<style>
  :root {
    --page: #e9ebee;
    --brand-blue: #1a74b0;
    --brand-blue-deep: #10609a;
    --brand-blue-light: #3aa2d2;
    --ink: #1c1c1c;
    --white: #ffffff;
    --divider: #2a7fb8;
  }
  * { box-sizing: border-box; margin: 0; padding: 0; }
  html, body {
    width: 1200px; height: 1000px; overflow: hidden;
    background: var(--page);
    font-family: "Open Sans", Arial, sans-serif;
  }
  .canvas { position: relative; width: 1200px; height: 1000px; }
  .card {
    position: absolute; left: 250px; width: 700px; height: 400px;
    border-radius: 34px; overflow: hidden;
    box-shadow: 0 6px 18px rgba(0,0,0,.18);
  }
  /* Front */
  .card--front { top: 70px; background: var(--brand-blue); }
  .front__art {
    position: absolute; inset: 0;
    background: radial-gradient(ellipse at 45% 40%, rgba(90,170,215,.45), rgba(26,116,176,0) 65%);
  }
  .front__brand {
    position: absolute; left: 90px; top: 140px;
    display: flex; align-items: center; gap: 18px;
  }
  .brand__dot { width: 34px; height: 34px; border-radius: 50%; background: var(--white); }
  .front__name { color: var(--white); font-weight: 700; font-size: 72px; letter-spacing: 2px; line-height: 1; }
  .front__slogan {
    position: absolute; left: 146px; top: 238px;
    color: var(--white); font-weight: 600; font-size: 19px; letter-spacing: 3px; text-transform: uppercase;
  }
  /* Back */
  .card--back { top: 530px; background: var(--white); }
  .back__brand {
    position: absolute; right: 40px; top: 34px; text-align: right;
  }
  .back__brand-row { display: flex; align-items: center; justify-content: flex-end; gap: 10px; }
  .back__brand-dot { width: 16px; height: 16px; border-radius: 50%; background: var(--brand-blue); }
  .back__brand-name { color: var(--brand-blue); font-weight: 700; font-size: 34px; letter-spacing: 1px; line-height: 1; }
  .back__brand-slogan { color: var(--brand-blue); font-size: 10px; font-weight: 600; letter-spacing: 1.5px; text-transform: uppercase; margin-top: 4px; }
  .identity { position: absolute; left: 40px; top: 150px; }
  .identity__company { font-weight: 700; font-size: 42px; line-height: 1; color: var(--ink); }
  .identity__company-accent { color: var(--brand-blue); }
  .identity__person { color: var(--brand-blue); font-weight: 600; font-size: 22px; margin-top: 10px; }
  .divider { position: absolute; left: 320px; top: 150px; width: 2px; height: 100px; background: var(--divider); }
  .contacts { position: absolute; left: 336px; top: 148px; list-style: none; }
  .contacts li { display: flex; align-items: center; gap: 8px; font-size: 17px; color: var(--ink); height: 34px; }
  .contacts svg { width: 18px; height: 18px; flex: none; }
  .band {
    position: absolute; left: 0; right: 0; bottom: 0; height: 72px;
    background: linear-gradient(90deg, var(--brand-blue-deep), var(--brand-blue-light) 55%, var(--brand-blue));
    display: flex; align-items: center; padding-left: 110px;
    color: var(--white); font-weight: 700; font-size: 26px;
  }
</style>
</head>
<body>
<div class="canvas">
  <section class="card card--front">
    <div class="front__art" role="img" aria-label="Faint blue illustration of car parts: tyres, brake discs, gears and engine components"></div>
    <div class="front__brand">
      <span class="brand__dot"></span>
      <span class="front__name">GearVista</span>
    </div>
    <div class="front__slogan">Quality Parts At Affordable Prices</div>
  </section>

  <section class="card card--back">
    <div class="back__brand">
      <div class="back__brand-row">
        <span class="back__brand-dot"></span>
        <span class="back__brand-name">GearVista</span>
      </div>
      <div class="back__brand-slogan">Quality Parts At Affordable Prices</div>
    </div>

    <div class="identity">
      <div class="identity__company"><span class="identity__company-accent">GEAR</span> VISTA</div>
      <div class="identity__person">Rohan Melwanikar</div>
    </div>
    <div class="divider"></div>
    <ul class="contacts">
      <li>
        <svg viewBox="0 0 18 18" aria-hidden="true"><rect x="5" y="1.5" width="8" height="15" rx="1.5" fill="none" stroke="#1a74b0" stroke-width="1.5"/><line x1="8" y1="14" x2="10" y2="14" stroke="#1a74b0" stroke-width="1.5"/></svg>
        246-319-8042
      </li>
      <li>
        <svg viewBox="0 0 18 18" aria-hidden="true"><rect x="1.5" y="4" width="15" height="10" fill="none" stroke="#1a74b0" stroke-width="1.5"/><polyline points="1.5,4 9,10 16.5,4" fill="none" stroke="#1a74b0" stroke-width="1.5"/></svg>
        gearvistabq@mailbox-example.test
      </li>
      <li>
        <svg viewBox="0 0 18 18" aria-hidden="true"><rect x="2" y="2" width="14" height="14" rx="2" fill="#1a74b0"/></svg>
        www.examplesocial.test/gearvistabq
      </li>
    </ul>

    <div class="band">Quality Parts At Affordable Prices</div>
  </section>
</div>
</body>
</html>
```